Verpackungen für Matcha Tee Sticks
Zielgruppe
Premium Matcha Tee Sticks in hochwertiger Qualität. Die Umverpackung wird voraussichtlich in Dosen sein.
Unsere Zielgruppe sind Menschen mit Lust auf guten Geschmack und eine Prise Luxus, ReisSportler, Gesundheitsbewusste und Genießer.
Aufgabenstellung
Wir brauchen ein Logo & eine Verpackung (Banderole) für Dosen (Durchmesser: 63/ Höhe: 105 mm) für unser Label 'teefix4go'.
Modern, Luxuriös, Schlicht - Farben: gold, grün, schwarz, weiß (sind aber auch für andere Farbvarianten offen)
Die Matcha Sticks werden wahrscheinlich in schwarzen oder weißen oder goldenen Dosen verkauft werden.
Abmessungen Banderole: ca. Höhe: 105 / Breite:178mm
@all: Tendenziell sollen die Vorschläge noch luxuriöser und feiner werden. z.B. schwarzer Hintergrund mit feiner Schrift oder z.B. die Marke QRP Brew aus Singapur hat erlesene Tees in luxuriösem Design. Inspirierende Marken: Belnoix Vamont (Kekse, Kerzen), Ulla Verbeck (Kosmetik), Tissand Oulmes (Tee), Brevo oder ZAR Tee....
Es darf gerne ein Eyecatcher sein, IT-piece, must-have.... Eine Dose, die man lieber sammelt als nach Gebrauch wegzuschmeißen. Ihr könnt Euch auch vom Farbschema lösen. Das war nur ein erster Gedanke, da Matcha grün ist und die Dose voraussichtlich schwarz und gold Luxus verkörpert. Stellt Euch die Einkaufsmall in Dubai vor. Da heißt es auffallen. Knallorange....es muss rocken.
Wir sind gespannt auf weitere Vorschläge und möchten uns auch für die eingegangen Vorschläge bedanken. Wir wissen, dass da schon einiges an Arbeit drinsteckt.
Happy Weekend :)

```html
<!DOCTYPE html>
<html lang="de">
<head>
<meta charset="utf-8">
<title>teefix4go – Logo &amp; Banderole Matcha Sticks</title>
<link rel="stylesheet" href="https://fonts.googleapis.com/css2?family=Playfair+Display:wght@400&family=Cinzel:wght@600&display=swap">
<style>
  :root {
    --paper: #ffffff;
    --ink: #141414;
    --band-black: #050505;
    --can-black: #1c1c1c;
    --green-dark: #0a3a1b;
    --green: #1a7536;
    --green-light: #2c9447;
    --gold: #d6b04a;
    --gold-light: #f2dc86;
    --gold-dark: #a07a2a;
    --ornament-grey: #3f3f3f;
    --ornament-grey-light: #5c5c5c;
  }
  * { margin: 0; padding: 0; box-sizing: border-box; }
  html, body { width: 849px; height: 1200px; overflow: hidden; background: var(--paper); }
  .sheet { position: relative; width: 849px; height: 1200px; }

  .logo-primary {
    position: absolute; left: 0; top: 112px; width: 849px;
    text-align: center;
    font-family: "Playfair Display", serif; font-weight: 400;
    font-size: 54px; line-height: 1; letter-spacing: 1px;
    color: var(--ink); white-space: nowrap;
  }

  .brand-band {
    position: absolute; left: 0; top: 282px; width: 849px; height: 190px;
    background: var(--band-black); overflow: hidden;
  }
  .brand-band svg, .label-flat, .can-label { display: block; }

  .label-flat { position: absolute; left: 103px; top: 627px; }
  .can-label { position: absolute; left: 439px; top: 558px; }

  .label-wordmark { font-family: "Playfair Display", serif; font-weight: 400; fill: var(--gold); }
  .product-name { font-family: "Cinzel", serif; font-weight: 600; fill: var(--gold); }
</style>
</head>
<body>
<main class="sheet">

  <p class="logo-primary">teefix4go</p>

  <section class="brand-band">
    <svg width="849" height="190" viewBox="0 0 849 190">
      <defs>
        <linearGradient id="band-ornament-fill" x1="0" y1="0" x2="1" y2="1">
          <stop offset="0" stop-color="var(--ornament-grey-light)"/>
          <stop offset="1" stop-color="var(--ornament-grey)"/>
        </linearGradient>
        <linearGradient id="band-gold-line" x1="0" x2="1">
          <stop offset="0" stop-color="var(--gold-dark)"/>
          <stop offset="0.5" stop-color="var(--gold-light)"/>
          <stop offset="1" stop-color="var(--gold-dark)"/>
        </linearGradient>
      </defs>
      <ellipse cx="413" cy="95" rx="190" ry="140" fill="url(#band-ornament-fill)" role="img" aria-label="Graues Mandala-Ornament hinter dem Logo"/>
      <g transform="translate(413 95) scale(96)">
        <polygon fill="var(--band-black)" stroke="url(#band-gold-line)" stroke-width="1.5" vector-effect="non-scaling-stroke"
          points="0.966,0.259 0.707,0.707 0.259,0.966 -0.259,0.966 -0.707,0.707 -0.966,0.259 -0.966,-0.259 -0.707,-0.707 -0.259,-0.966 0.259,-0.966 0.707,-0.707 0.966,-0.259"/>
      </g>
      <text class="label-wordmark" x="413" y="106" font-size="32" text-anchor="middle">teefix4go</text>
    </svg>
  </section>

  <svg class="label-flat" width="173" height="416" viewBox="0 0 173 416">
    <defs>
      <linearGradient id="flat-green" x1="0" x2="1">
        <stop offset="0" stop-color="var(--green-dark)"/>
        <stop offset="0.5" stop-color="var(--green)"/>
        <stop offset="1" stop-color="var(--green-dark)"/>
      </linearGradient>
      <linearGradient id="gold-fill" x1="0" y1="0" x2="1" y2="1">
        <stop offset="0" stop-color="var(--gold-light)"/>
        <stop offset="0.5" stop-color="var(--gold)"/>
        <stop offset="1" stop-color="var(--gold-dark)"/>
      </linearGradient>
      <linearGradient id="gold-strip" x1="0" x2="1">
        <stop offset="0" stop-color="var(--gold-dark)"/>
        <stop offset="0.5" stop-color="var(--gold-light)"/>
        <stop offset="1" stop-color="var(--gold-dark)"/>
      </linearGradient>
      <clipPath id="flat-clip"><rect width="173" height="416"/></clipPath>
    </defs>
    <g clip-path="url(#flat-clip)">
      <rect width="173" height="416" fill="var(--can-black)"/>
      <rect y="64" width="173" height="324" fill="url(#flat-green)"/>
      <text class="label-wordmark" x="86.5" y="40" font-size="12" text-anchor="middle">teefix4go</text>
      <line x1="0" y1="46" x2="173" y2="46" stroke="var(--gold)" stroke-width="0.8"/>
      <rect x="14" y="78" width="145" height="5" fill="url(#gold-strip)" role="img" aria-label="Reihe kleiner goldener Ornamentmotive"/>
      <circle cx="86.5" cy="240" r="104" fill="url(#gold-fill)" role="img" aria-label="Goldenes Mandala-Ornament"/>
      <circle cx="86.5" cy="240" r="68" fill="none" stroke="var(--green-dark)" stroke-width="0.8" opacity="0.5"/>
      <g transform="translate(86.5 240) scale(56)">
        <polygon fill="var(--can-black)" stroke="var(--gold-light)" stroke-width="1.2" vector-effect="non-scaling-stroke"
          points="0.966,0.259 0.707,0.707 0.259,0.966 -0.259,0.966 -0.707,0.707 -0.966,0.259 -0.966,-0.259 -0.707,-0.707 -0.259,-0.966 0.259,-0.966 0.707,-0.707 0.966,-0.259"/>
      </g>
      <text class="product-name" x="86.5" y="242" font-size="19" text-anchor="middle">MATCHA</text>
      <text class="product-name" x="86.5" y="258" font-size="12" letter-spacing="4" text-anchor="middle">STICKS</text>
      <rect x="14" y="390" width="145" height="5" fill="url(#gold-strip)" role="img" aria-label="Reihe kleiner goldener Ornamentmotive"/>
    </g>
  </svg>

  <svg class="can-label" width="239" height="598" viewBox="0 0 239 598">
    <defs>
      <linearGradient id="can-green" x1="0" x2="1">
        <stop offset="0" stop-color="var(--green-dark)"/>
        <stop offset="0.5" stop-color="var(--green-light)"/>
        <stop offset="1" stop-color="var(--green-dark)"/>
      </linearGradient>
      <clipPath id="can-clip"><rect width="239" height="598"/></clipPath>
    </defs>
    <g clip-path="url(#can-clip)">
      <rect width="239" height="598" fill="var(--can-black)"/>
      <rect y="105" width="239" height="434" fill="url(#can-green)"/>
      <text class="label-wordmark" x="119.5" y="62" font-size="15" text-anchor="middle">teefix4go</text>
      <line x1="0" y1="70" x2="239" y2="70" stroke="var(--gold)" stroke-width="0.8"/>
      <rect x="16" y="110" width="207" height="6" fill="url(#gold-strip)" role="img" aria-label="Reihe kleiner goldener Ornamentmotive"/>
      <circle cx="119.5" cy="340" r="150" fill="url(#gold-fill)" role="img" aria-label="Goldenes Mandala-Ornament"/>
      <circle cx="119.5" cy="340" r="108" fill="none" stroke="var(--green-dark)" stroke-width="1" opacity="0.5"/>
      <g transform="translate(119.5 340) scale(90)">
        <polygon fill="var(--can-black)" stroke="var(--gold-light)" stroke-width="1.5" vector-effect="non-scaling-stroke"
          points="0.966,0.259 0.707,0.707 0.259,0.966 -0.259,0.966 -0.707,0.707 -0.966,0.259 -0.966,-0.259 -0.707,-0.707 -0.259,-0.966 0.259,-0.966 0.707,-0.707 0.966,-0.259"/>
      </g>
      <text class="product-name" x="119.5" y="335" font-size="27" letter-spacing="1" text-anchor="middle">MATCHA</text>
      <text class="product-name" x="119.5" y="361" font-size="18" letter-spacing="6" text-anchor="middle">STICKS</text>
      <rect x="16" y="540" width="207" height="6" fill="url(#gold-strip)" role="img" aria-label="Reihe kleiner goldener Ornamentmotive"/>
    </g>
  </svg>

</main>
</body>
</html>
```